Existing Logo Post Card Design for Residential and Commercial Services Company

We are looking for a Post card design for bulk mail along with letterhead and business cards for a new Residential and Commercial Services company. We focus on senior citizens and vets with the idea of "One Call Every Service". We provide landscaping, pressure washing, maid service, and pest control to both the commercial and residential market. We also provide estimates, proposal creation, scheduling, cost controls and consulting to contractors.
The mailer is going to be targeting the residential services portion of the business and heading out to advertise our landscaping, pressure washing and maid services. It should use the primary color of red, white and blue. If the logo need to be tweaked on shades, please feel free to do that. More than just service we sell security to our customers because we are not the average residential services company.
The sample business card designs that have been uploaded are from another company that we currently own and we like the cards. We would like to keep it simple on the back of the card with the colors and the company slogan of “One Call Every Service”.
We also like the layout of the front of the card with the logo boldly displayed. The company name should also be display on the card “Trellmark Hollow” Please make sure there is a name, address, phone number, email address and website www.trellmarkhollow.example on the front of the card as well.
We would like the letter head to display the logo in the top left of the page with space for phone number, address, and website at the bottom of the page. We would like the info at the bottom of the page to be in a straight line across the bottom of the page. The page dimensions should be 8.5X11” and there should be a .5” margin around the complete perimeter of the page.
Thanks and good luck

Target Market(s)

Homeowners with a focus on Senior citizens and Vets

Industry/Entity Type

Residential Construction

Contact Information for Business Card

The business card should focus on Red, white and blue it will be 2 sided and should be bold and will be foiled.

Font styles to use
Serif

Requirements
Must have
• The Company slogan should be displayed on the back side of the card "One Call Every Service" it should also be easy to read
Nice to have
• The card should be Red, White, Blue and primarily black text.
Should not have
• Please refrain hard to read text it should be clear and easy to read

```html
<!DOCTYPE html>
<html lang="en">
<head>
<meta charset="utf-8">
<title>Trellmark Hollow – Letterhead Set</title>
<link rel="stylesheet" href="https://fonts.googleapis.com/css2?family=Raleway:wght@600;700;800&display=swap">
<style>
  :root {
    --brand-red: #c01f33;
    --brand-blue: #1f3f98;
    --paper: #ffffff;
    --backdrop: #ece7df;
    --rule: #d9596a;
  }
  * { margin: 0; padding: 0; box-sizing: border-box; }
  html, body { width: 1200px; height: 729px; overflow: hidden; }
  body {
    position: relative;
    background: var(--backdrop);
    font-family: "Raleway", Arial, sans-serif;
  }
  .sheet {
    position: absolute;
    top: 148px;
    width: 346px;
    height: 488px;
    background: var(--paper);
    box-shadow: 0 2px 8px rgba(0,0,0,0.25);
    overflow: hidden;
  }
  .sheet--corner { left: 51px; }
  .sheet--centered { left: 422px; }
  .sheet--banded { left: 791px; }

  .sheet__shapes {
    position: absolute;
    inset: 0;
    width: 100%;
    height: 100%;
  }
  .fill-red { fill: var(--brand-red); }
  .fill-blue { fill: var(--brand-blue); }

  .wordmark {
    position: absolute;
    font-weight: 800;
    font-size: 19px;
    letter-spacing: 0.5px;
    color: var(--brand-red);
    white-space: nowrap;
    text-transform: uppercase;
  }
  .sheet--corner .wordmark { left: 22px; top: 38px; }
  .sheet--centered .wordmark { left: 0; right: 0; top: 22px; text-align: center; }
  .sheet--banded .wordmark { left: 26px; top: 26px; }

  .header-rule {
    position: absolute;
    left: 23px; right: 23px; top: 54px;
    height: 1px;
    background: var(--rule);
  }

  .contact { position: absolute; font-size: 6.6px; font-weight: 700; }
  .contact__item { display: inline-flex; align-items: center; gap: 3px; white-space: nowrap; }
  .contact__icon { width: 8px; height: 8px; flex: none; }

  .contact--stack { left: 22px; top: 413px; color: #fff; }
  .contact--stack .contact__item { display: flex; margin-bottom: 5px; }

  .contact--rows { left: 0; right: 0; text-align: center; }
  .contact--rows .contact__row { display: flex; justify-content: center; gap: 6px; margin-bottom: 3px; }
  .sheet--centered .contact--rows { top: 432px; color: var(--brand-blue); }
  .sheet--banded .contact--rows { top: 451px; color: #fff; }

  .icon-disc { fill: currentColor; }
  .contact--on-light .icon-disc { fill: var(--brand-red); }
  .icon-glyph { fill: var(--brand-red); }
  .contact--on-light .icon-glyph { fill: #fff; }
</style>
</head>
<body>
<svg width="0" height="0" style="position:absolute" aria-hidden="true">
  <defs>
    <symbol id="icon-phone" viewBox="0 0 10 10">
      <circle class="icon-disc" cx="5" cy="5" r="5"/>
      <path class="icon-glyph" d="M3.2 2.4l1 0.9-0.5 0.8c0.4 0.8 1 1.4 1.8 1.8l0.8-0.5 0.9 1-0.6 0.9C4.5 7.1 2.9 5.5 2.5 3.2z"/>
    </symbol>
    <symbol id="icon-mail" viewBox="0 0 10 10">
      <circle class="icon-disc" cx="5" cy="5" r="5"/>
      <path class="icon-glyph" d="M2.6 3.3h4.8v3.4H2.6z M2.9 3.6L5 5.1 7.1 3.6" />
    </symbol>
    <symbol id="icon-pin" viewBox="0 0 10 10">
      <circle class="icon-disc" cx="5" cy="5" r="5"/>
      <path class="icon-glyph" d="M5 2.2a1.9 1.9 0 0 1 1.9 1.9C6.9 5.5 5 7.8 5 7.8S3.1 5.5 3.1 4.1A1.9 1.9 0 0 1 5 2.2z"/>
    </symbol>
    <symbol id="icon-web" viewBox="0 0 10 10">
      <circle class="icon-disc" cx="5" cy="5" r="5"/>
      <circle class="icon-glyph" cx="5" cy="5" r="2.4"/>
      <circle class="icon-disc" cx="5" cy="5" r="1.3"/>
    </symbol>
  </defs>
</svg>

<!-- Letterhead A: corner blocks -->
<section class="sheet sheet--corner" aria-label="Letterhead with corner blocks">
  <svg class="sheet__shapes" viewBox="0 0 346 488" aria-hidden="true">
    <polygon class="fill-blue" points="0,0 185,0 178,24 0,24"/>
    <polygon class="fill-red" points="166,0 346,0 346,37 184,37"/>
    <polygon class="fill-red" points="0,362 332,488 0,488"/>
    <polygon class="fill-blue" points="222,448 346,418 346,488 332,488"/>
  </svg>
  <div class="wordmark">Trellmark Hollow</div>
  <div class="contact contact--stack">
    <span class="contact__item"><svg class="contact__icon"><use href="#icon-phone"/></svg>+40 555 010 203</span>
    <span class="contact__item"><svg class="contact__icon"><use href="#icon-mail"/></svg>hello@trellmark.example</span>
    <span class="contact__item"><svg class="contact__icon"><use href="#icon-pin"/></svg>location and adress</span>
    <span class="contact__item"><svg class="contact__icon"><use href="#icon-web"/></svg>www.trellmarkhollow.example</span>
  </div>
</section>

<!-- Letterhead B: centred header -->
<section class="sheet sheet--centered" aria-label="Letterhead with centred header">
  <svg class="sheet__shapes" viewBox="0 0 346 488" aria-hidden="true">
    <polygon class="fill-red" points="0,440 150,488 0,488"/>
    <polygon class="fill-blue" points="70,488 346,456 346,488"/>
  </svg>
  <div class="wordmark">Trellmark Hollow</div>
  <div class="header-rule"></div>
  <div class="contact contact--rows contact--on-light">
    <div class="contact__row">
      <span class="contact__item"><svg class="contact__icon"><use href="#icon-phone"/></svg>+40 555 010 203</span>
      <span class="contact__item"><svg class="contact__icon"><use href="#icon-mail"/></svg>hello@trellmark.example</span>
    </div>
    <div class="contact__row">
      <span class="contact__item"><svg class="contact__icon"><use href="#icon-pin"/></svg>location and adress</span>
      <span class="contact__item"><svg class="contact__icon"><use href="#icon-web"/></svg>www.trellmarkhollow.example</span>
    </div>
  </div>
</section>

<!-- Letterhead C: footer band -->
<section class="sheet sheet--banded" aria-label="Letterhead with footer band">
  <svg class="sheet__shapes" viewBox="0 0 347 488" aria-hidden="true">
    <polygon class="fill-blue" points="0,430 347,413 347,427 0,442"/>
    <polygon class="fill-red" points="0,442 347,427 347,488 0,488"/>
  </svg>
  <div class="wordmark">Trellmark Hollow</div>
  <div class="contact contact--rows">
    <div class="contact__row">
      <span class="contact__item"><svg class="contact__icon"><use href="#icon-phone"/></svg>+40 555 010 203</span>
      <span class="contact__item"><svg class="contact__icon"><use href="#icon-mail"/></svg>hello@trellmark.example</span>
    </div>
    <div class="contact__row">
      <span class="contact__item"><svg class="contact__icon"><use href="#icon-pin"/></svg>location and adress</span>
      <span class="contact__item"><svg class="contact__icon"><use href="#icon-web"/></svg>www.trellmarkhollow.example</span>
    </div>
  </div>
</section>
</body>
</html>
```